New business Cards

We need some new cards that stand out. We love our logo and colour scheme but need to incorporate a numo logo and ptl logo yet still keep our cards uncluttered and clean looking.
Our tag is Keen Ledgerworks. Anywhere, Anytime.
The idea of the cards is to show authority in accounting and Numo/ cloud software

```html
<!DOCTYPE html>
<html lang="en">
<head>
<meta charset="utf-8">
<title>Marlow Business Solutions – Business Cards</title>
<link rel="stylesheet" href="https://fonts.googleapis.com/css2?family=Open+Sans:wght@400;600;700&display=swap">
<style>
  :root {
    --backdrop: #ecebe8;
    --green-deep: #1f5a22;
    --green-mid: #3f8f3a;
    --green-light: #6bbf59;
    --green-text: #5cae4c;
    --ink: #1c1c1c;
    --grey: #555555;
    --white: #ffffff;
    --teal: #1aa3c4;
    --teal-dark: #0f7f93;
    --badge-blue: #1a4f9c;
  }
  * { box-sizing: border-box; margin: 0; padding: 0; }
  html, body {
    width: 1200px; height: 784px; overflow: hidden;
    background: var(--backdrop);
    font-family: "Open Sans", Arial, sans-serif;
  }
  .sheet {
    position: relative; width: 1200px; height: 784px;
    display: flex; align-items: center; justify-content: center; gap: 40px;
  }
  .card {
    position: relative; width: 560px; height: 320px;
    box-shadow: 0 6px 18px rgba(0,0,0,0.18);
    overflow: hidden;
  }

  /* Front */
  .card-front { color: var(--white); }
  .card-front .pattern {
    position: absolute; inset: 0;
    background: radial-gradient(ellipse at 75% 35%, var(--green-light) 0%, var(--green-mid) 45%, var(--green-deep) 100%);
  }
  .front-brand {
    position: absolute; left: 50%; top: 46px; transform: translateX(-50%);
    display: flex; align-items: center; gap: 12px;
  }
  .brand-square { width: 62px; height: 62px; background: var(--white); }
  .brand-name {
    font-weight: 600; font-size: 28px; letter-spacing: 4px; line-height: 1;
  }
  .brand-name small {
    display: block; font-size: 13px; letter-spacing: 1px; margin-top: 6px;
  }
  .tagline {
    position: absolute; left: 0; right: 0; top: 178px; text-align: center;
    font-size: 17px; letter-spacing: 4px; font-weight: 400;
  }

  /* Back */
  .card-back { background: var(--white); }
  .back-brand {
    position: absolute; left: 34px; top: 34px;
    display: flex; align-items: center; gap: 12px;
  }
  .back-brand .brand-square { background: var(--green-light); width: 76px; height: 76px; }
  .back-brand .brand-name { color: var(--grey); font-size: 30px; }
  .back-brand .brand-name small { color: var(--green-text); font-size: 13px; }

  .person { position: absolute; left: 34px; top: 150px; }
  .person-name { color: var(--green-text); font-size: 19px; font-weight: 400; }
  .person-role { color: var(--ink); font-size: 14px; margin-top: 2px; }

  .contact { position: absolute; left: 34px; top: 214px; list-style: none; }
  .contact li {
    display: flex; align-items: center; gap: 8px;
    font-size: 14.5px; font-weight: 600; color: var(--ink); line-height: 20px;
  }
  .contact svg { width: 14px; height: 14px; flex: none; }
  .contact .no-icon { padding-left: 22px; }

  .badges { position: absolute; right: 30px; top: 110px; width: 118px; }
  .badge-row { display: flex; gap: 8px; }
  .badge-circle { width: 52px; height: 52px; border-radius: 50%; background: var(--teal); }
  .badge-circle.alt { background: var(--teal-dark); }
  .badge-block { width: 112px; height: 56px; background: var(--badge-blue); margin-top: 10px; }
</style>
</head>
<body>
<main class="sheet">

  <section class="card card-front" aria-label="Card front">
    <div class="pattern" role="img" aria-label="Green pattern of receding ovals"></div>
    <div class="front-brand">
      <span class="brand-square"></span>
      <span class="brand-name">MARLOW<small>business solutions</small></span>
    </div>
    <p class="tagline">KEEN LEDGERWORKS. ANYWHERE, ANYTIME.</p>
  </section>

  <section class="card card-back" aria-label="Card back">
    <div class="back-brand">
      <span class="brand-square"></span>
      <span class="brand-name">MARLOW<small>business solutions</small></span>
    </div>

    <div class="person">
      <p class="person-name">Helen Marlow, PTL, CTA</p>
      <p class="person-role">Partner</p>
    </div>

    <ul class="contact">
      <li>
        <svg viewBox="0 0 16 16" aria-hidden="true"><path fill="#5cae4c" d="M3.5 1.5l2.5 3-1.5 1.5c.8 1.8 2.2 3.2 4 4l1.5-1.5 3 2.5-1.5 2.5C6.5 13.5 2.5 9.5 1 4z"/></svg>
        03 5100 2290
      </li>
      <li>
        <svg viewBox="0 0 16 16" aria-hidden="true"><rect x="1" y="3.5" width="14" height="9" fill="#5cae4c"/><path d="M1 3.5l7 5 7-5" stroke="#fff" stroke-width="1.3" fill="none"/></svg>
        helenm@marlowbussol.com.au
      </li>
      <li>
        <svg viewBox="0 0 16 16" aria-hidden="true"><circle cx="8" cy="8" r="6.5" fill="none" stroke="#5cae4c" stroke-width="1.6"/><path d="M1.5 8h13M8 1.5c-3 3.5-3 9.5 0 13M8 1.5c3 3.5 3 9.5 0 13" stroke="#5cae4c" stroke-width="1.2" fill="none"/></svg>
        www.marlowbussol.com.au
      </li>
      <li class="no-icon">Brenton Vic 3999</li>
    </ul>

    <div class="badges" aria-label="Partner and membership badges">
      <div class="badge-row">
        <span class="badge-circle"></span>
        <span class="badge-circle alt"></span>
      </div>
      <div class="badge-block"></div>
    </div>
  </section>

</main>
</body>
</html>
```